Open Meadow, Weekly therapy lessons for the heart of a sister missionary

This is a weekly guided therapy book for female Mormon missionaries. They leave for their missions for 18 months and I am a psychotherapist that is creating a guided workbook to help them through mental health struggles on their mission. I need a good book cover, also preferably something for the spine and back as well. I would like something that gives a soft and safe feeling.

```html
<!DOCTYPE html>
<html lang="en">
<head>
<meta charset="utf-8">
<title>Open Meadow – Book Cover Spread</title>
<link href="https://fonts.googleapis.com/css2?family=Great+Vibes&family=Libre+Baskerville&display=swap" rel="stylesheet">
<style>
  :root {
    --paper: #ffffff;
    --heart-red: #d0212b;
    --ink: #111111;
    --lamp-dark: #1a1a1a;
    --lamp-glow: #f5d61c;
  }
  html, body {
    margin: 0;
    padding: 0;
    overflow: hidden;
    background: var(--paper);
  }
  .spread {
    position: relative;
    width: 1200px;
    height: 864px;
    background: var(--paper);
    overflow: hidden;
    font-family: "Libre Baskerville", Georgia, serif;
    color: var(--ink);
  }
  .script {
    font-family: "Great Vibes", cursive;
    color: var(--heart-red);
    font-weight: 400;
    white-space: nowrap;
    margin: 0;
    position: absolute;
    line-height: 1;
  }

  /* Back cover */
  .back-title-first { left: 100px; top: 232px; font-size: 64px; }
  .back-title-second { left: 372px; top: 232px; font-size: 62px; }
  .lantern-art {
    position: absolute;
    left: 268px; top: 180px;
    width: 88px; height: 195px;
    border-radius: 40px 40px 18px 18px;
    background: linear-gradient(180deg, #f4f4f4 0%, var(--lamp-dark) 35%, var(--lamp-glow) 60%, var(--lamp-dark) 85%);
  }
  .back-quote {
    position: absolute;
    left: 40px; width: 500px;
    top: 397px;
    margin: 0;
    text-align: center;
    font-size: 25px;
    line-height: 29px;
  }
  .back-heart {
    position: absolute;
    left: 177px; top: 522px;
    width: 220px; height: 187px;
  }

  /* Spine */
  .spine-title {
    left: 584px; top: 338px;
    font-size: 40px;
    writing-mode: vertical-rl;
  }

  /* Front cover */
  .front-title { left: 660px; top: 100px; font-size: 96px; }
  .front-rule {
    position: absolute;
    left: 664px; top: 215px;
    width: 496px; height: 36px;
  }
  .front-subtitle {
    position: absolute;
    left: 669px; top: 272px;
    margin: 0;
    font-size: 28px;
    line-height: 33px;
    font-weight: 400;
  }
  .front-heart {
    position: absolute;
    left: 647px; top: 367px;
    width: 530px; height: 449px;
  }
  .reader-art {
    position: absolute;
    left: 689px; top: 432px;
    width: 392px; height: 334px;
    border-radius: 140px 60px 40px 120px;
    background: linear-gradient(160deg, #2a1a1a 0%, #6e1418 55%, #1b1b1b 100%);
  }
</style>
</head>
<body>
<main class="spread">

  <section class="back-cover">
    <p class="script back-title-first">Open</p>
    <div class="lantern-art" role="img" aria-label="Illustration of an old oil lantern with a glowing yellow glass"></div>
    <p class="script back-title-second">Meadow</p>
    <p class="back-quote">“Let your light shine in the darkness<br>and your heart be filled with peace”</p>
    <svg class="back-heart" viewBox="0 0 100 85" preserveAspectRatio="none" aria-hidden="true">
      <path fill="var(--heart-red)" d="M50 13 C41 2 24 -1 12 6 C0 14 -1 34 8 48 C20 65 38 76 50 85 C62 76 80 65 92 48 C101 34 100 14 88 6 C76 -1 59 2 50 13Z"/>
    </svg>
  </section>

  <section class="spine">
    <p class="script spine-title">Open Meadow</p>
  </section>

  <section class="front-cover">
    <h1 class="script front-title">Open Meadow</h1>
    <svg class="front-rule" viewBox="0 0 496 36" aria-hidden="true">
      <path d="M2 30 C120 8 220 0 300 8 C380 16 450 24 494 16" fill="none" stroke="var(--heart-red)" stroke-width="3.5" stroke-linecap="round"/>
    </svg>
    <h2 class="front-subtitle">Weekly therapy lessons<br>for the heart of&nbsp; sister missionary</h2>
    <svg class="front-heart" viewBox="0 0 100 85" preserveAspectRatio="none" aria-hidden="true">
      <path fill="var(--heart-red)" d="M50 13 C41 2 24 -1 12 6 C0 14 -1 34 8 48 C20 65 38 76 50 85 C62 76 80 65 92 48 C101 34 100 14 88 6 C76 -1 59 2 50 13Z"/>
    </svg>
    <div class="reader-art" role="img" aria-label="Stencil-style illustration of a young woman in a patterned dress sitting and reading a book"></div>
  </section>

</main>
</body>
</html>
```